Sign Advertisment for Condominium Development

I need a sign created that will be placed in front of a building that is being converted into a luxury condominium development.

The sign needs to say:

Two, Boutique Luxury Condominiums Delivering late 2015.

Luxury Finishes // Designer Kitchens and Bath // Each Unit over 2,000 Square Feet

Deeded Parking Included with Each Unit

To Learn More, Contact:

Loretta Pinwell or Morgan Tesh
(202) 555-0147
Loretta.Pinwell@nrg-example.com

I need a small disclaimer at the bottom stating:

These Condominium(s) have not been registered by the Office of Residential Property Oversight Bureau of Dwelling Registration Tenancy Transfer and Purchase Section. A Condominium Unit may be reserved on a non-binding reservation agreement, but no contract of sale or lease that is binding on the purchaser may be entered into prior to registration.

Target Market(s)

Young professionals seeking luxury condominium

Industry/Entity Type

Building

Font styles to use
Serif

Colors
00a88f
ffffff

```html
<!DOCTYPE html>
<html lang="en">
<head>
<meta charset="utf-8">
<title>Northgate Fine Properties – Boutique Luxury Condominiums</title>
<link rel="stylesheet" href="https://fonts.googleapis.com/css2?family=Open+Sans:wght@300;400&display=swap">
<style>
  :root {
    --navy: #2b2a48;
    --navy-panel: rgba(40, 38, 70, 0.93);
    --white: #ffffff;
    --band: rgba(255, 255, 255, 0.82);
    --footer: rgba(238, 236, 234, 0.88);
    --ink: #2a2944;
    --muted: #8a8a94;
    --room-light: #f3f3f1;
    --room-mid: #d8d6d2;
    --counter: #6d6660;
  }
  * { box-sizing: border-box; margin: 0; padding: 0; }
  html, body { width: 1200px; height: 800px; overflow: hidden; }
  body { font-family: "Open Sans", sans-serif; color: var(--ink); }

  .sign { position: relative; width: 1200px; height: 800px; overflow: hidden; }

  .interior-photo {
    position: absolute; inset: 0;
    background:
      linear-gradient(90deg, rgba(60,70,50,0.35) 0%, rgba(60,70,50,0) 14%, rgba(0,0,0,0) 86%, rgba(120,100,80,0.35) 100%),
      linear-gradient(180deg, var(--room-light) 0%, #ecebe8 40%, var(--room-mid) 58%, var(--counter) 75%, #8d8882 100%);
  }

  .brand-tab {
    position: absolute; left: 473px; top: 0; width: 234px; height: 183px;
    background: var(--navy);
    border-radius: 0 0 44px 44px;
    display: flex; align-items: center; justify-content: center;
    padding: 50px 20px 0;
    text-align: center;
  }
  .brand-name {
    color: var(--white); font-weight: 400; font-size: 20px; line-height: 28px;
  }

  .headline-band {
    position: absolute; left: 85px; top: 253px; width: 1030px; height: 95px;
    background: var(--band);
    border-bottom: 1px solid rgba(43,42,72,0.5);
    display: flex; align-items: center; justify-content: center;
  }
  .headline { font-weight: 300; font-size: 37px; color: var(--ink); white-space: nowrap; }

  .feature-list { list-style: none; }
  .feature {
    position: absolute; top: 354px; height: 179px;
    background: var(--navy-panel);
    color: var(--white);
    text-align: center; font-weight: 300; font-size: 24px; line-height: 33px;
    padding-top: 37px;
  }
  .feature svg { display: block; margin: 0 auto 11px; }
  .feature-1 { left: 89px; width: 250px; }
  .feature-2 { left: 347px; width: 250px; }
  .feature-3 { left: 604px; width: 251px; }
  .feature-4 { left: 863px; width: 250px; }

  .footer {
    position: absolute; left: 0; top: 660px; width: 1200px; height: 140px;
    background: var(--footer);
    text-align: center;
  }
  .disclaimer {
    width: 1030px; margin: 12px auto 0;
    font-size: 11px; line-height: 17px; color: var(--muted);
  }
  .contact-heading { margin-top: 34px; font-size: 19px; font-weight: 400; color: var(--ink); }
  .contact-line { margin-top: 1px; font-size: 14.5px; color: var(--ink); word-spacing: 1px; }
  .contact-line .sep { margin: 0 20px; }
</style>
</head>
<body>
<main class="sign">
  <div class="interior-photo" role="img" aria-label="Bright modern condominium interior with tall windows, pendant lights and a stone kitchen counter"></div>

  <header class="brand-tab">
    <span class="brand-name">Northgate Fine Properties</span>
  </header>

  <div class="headline-band">
    <h1 class="headline">Two, Boutique Luxury Condominiums Delivering late 2015.</h1>
  </div>

  <ul class="feature-list">
    <li class="feature feature-1">
      <svg width="22" height="20" viewBox="0 0 22 20" aria-hidden="true"><path d="M2 11 L8 17 L20 2" fill="none" stroke="#fff" stroke-width="4" stroke-linecap="round" stroke-linejoin="round"/></svg>
      Luxury Finishes
    </li>
    <li class="feature feature-2">
      <svg width="22" height="20" viewBox="0 0 22 20" aria-hidden="true"><path d="M2 11 L8 17 L20 2" fill="none" stroke="#fff" stroke-width="4" stroke-linecap="round" stroke-linejoin="round"/></svg>
      Designer Kitchens<br>and Bath
    </li>
    <li class="feature feature-3">
      <svg width="22" height="20" viewBox="0 0 22 20" aria-hidden="true"><path d="M2 11 L8 17 L20 2" fill="none" stroke="#fff" stroke-width="4" stroke-linecap="round" stroke-linejoin="round"/></svg>
      Each Unit over<br>2,000 Square Feet
    </li>
    <li class="feature feature-4">
      <svg width="22" height="20" viewBox="0 0 22 20" aria-hidden="true"><path d="M2 11 L8 17 L20 2" fill="none" stroke="#fff" stroke-width="4" stroke-linecap="round" stroke-linejoin="round"/></svg>
      Deeded Parking<br>Included with Each<br>Unit
    </li>
  </ul>

  <footer class="footer">
    <p class="disclaimer">These Condominium(s) have not been registered by the Office of Residential Property Oversight Bureau of Dwelling Registration Tenancy Transfer and Purchase Section. A Condominium Unit may be reserved on a non-binding reservation agreement, but no contract of sale or lease that is binding on the purchaser may be entered into prior to registration.</p>
    <h2 class="contact-heading">To Learn More, Contact:</h2>
    <p class="contact-line">Loretta Pinwell or Morgan Tesh<span class="sep">|</span>(202) 555-0147<span class="sep">|</span>Loretta.Pinwell@nrg-example.com</p>
  </footer>
</main>
</body>
</html>
```